Lena Corvell Business Card

I need a business card that reflects my current website: itslenacorvell.example and screenshot attached. If we keep the color scheme of the site and sample card below that would be ideal. The business card should include the information on the attached sample cards.

Industry/Entity Type

Business

```html
<!DOCTYPE html>
<html lang="en">
<head>
<meta charset="utf-8">
<title>Lena Corvell Business Card</title>
<link rel="stylesheet" href="https://fonts.googleapis.com/css2?family=Josefin+Sans:wght@400;600&display=swap">
<style>
  :root {
    --teal: #5dd1b6;
    --teal-light: #74dbc4;
    --charcoal: #404040;
    --ink: #111111;
    --paper: #ffffff;
    --photo-top: #8d8a87;
    --photo-bottom: #5f5c5a;
  }
  * { margin: 0; padding: 0; box-sizing: border-box; }
  html, body { width: 1200px; height: 757px; overflow: hidden; background: var(--paper); }
  .card {
    position: relative;
    width: 1200px;
    height: 757px;
    overflow: hidden;
    background: var(--paper);
    font-family: "Josefin Sans", sans-serif;
    color: var(--ink);
  }
  .header-band { position: absolute; left: 0; top: 0; width: 1200px; height: 432px; background: var(--teal); }
  .header-dots { position: absolute; inset: 0; }
  .divider-band { position: absolute; left: 0; top: 432px; width: 1200px; height: 100px; background: var(--charcoal); }
  .wordmark {
    position: absolute;
    left: 0; width: 1145px;
    top: 170px;
    text-align: center;
    font-size: 92px;
    font-weight: 400;
    letter-spacing: 1px;
    color: var(--ink);
  }
  .titles {
    position: absolute;
    left: 0; width: 1145px;
    top: 312px;
    text-align: center;
    list-style: none;
    font-size: 24px;
    font-variant: small-caps;
    letter-spacing: 3px;
    line-height: 31px;
  }
  .site-preview {
    position: absolute;
    left: 19px; top: 445px;
    width: 588px; height: 312px;
    background: linear-gradient(160deg, var(--photo-top), var(--photo-bottom));
  }
  .social {
    position: absolute;
    left: 770px; top: 494px;
    display: flex; gap: 16px;
    list-style: none;
  }
  .social-item { display: flex; flex-direction: column; align-items: center; width: 76px; }
  .social-square { width: 75px; height: 75px; background: var(--teal); border-radius: 8px; }
  .social-name { margin-top: 4px; font-size: 13px; font-weight: 600; color: var(--teal); }
  .contact {
    position: absolute;
    left: 620px; width: 560px;
    top: 596px;
    list-style: none;
    text-align: center;
    font-size: 26px;
    letter-spacing: 3px;
    line-height: 50px;
    text-transform: uppercase;
  }
</style>
</head>
<body>
<main class="card">
  <div class="header-band">
    <svg class="header-dots" width="1200" height="432" viewBox="0 0 1200 432" aria-hidden="true">
      <g fill="var(--teal-light)">
        <circle cx="178" cy="72" r="84"/>
        <circle cx="872" cy="60" r="138"/>
        <circle cx="523" cy="225" r="96"/>
        <circle cx="20" cy="298" r="66"/>
        <circle cx="1030" cy="408" r="74"/>
      </g>
    </svg>
    <h1 class="wordmark">iam Lena Corvell</h1>
    <ul class="titles">
      <li>LENA CORVELL Brand Curator</li>
      <li>Digital Storyteller</li>
      <li>Social Entrprenuer</li>
    </ul>
  </div>
  <div class="divider-band"></div>
  <div class="site-preview" role="img" aria-label="Website homepage preview with portrait photo and handwritten introduction"></div>
  <ul class="social">
    <li class="social-item"><span class="social-square"></span><span class="social-name">Pagefeed</span></li>
    <li class="social-item"><span class="social-square"></span><span class="social-name">Chirpline</span></li>
    <li class="social-item"><span class="social-square"></span><span class="social-name">Worknet</span></li>
  </ul>
  <ul class="contact">
    <li>@lenacorvell.example</li>
    <li>www.itslenacorvell.example</li>
    <li>555.010.4827</li>
  </ul>
</main>
</body>
</html>
```